Flyer-Design für Kanutouristiker (Kanu Vermietung) Folgeaufträge!!
Zielgruppe
Wir veranstalten Kanu - und Erlebnistouren. Vermieten Kanus, Schlauchboote (Rafts), SUP (Stand up Paddling) und Fahrräder.
Für Gruppen, Betriebe, Schulklassen, Vereine, Familien, Junggesellenabschiede, Geburtstage usw.
Aufgabenstellung
Wir möchten einen ansprechenden Flyer erstellen lassen, der Lust auf unsere Angebote machen soll.
Hier handelt es sich um einen DIN lang (A4) Wickelfalz Falter (6 Seiter)
Mit unseren Angeboten. Beispielbilder sind im Anhang mithochgeladen. Es können weitere geliefert werden- oder Sie sehen sich einmal auf unserer Webseite um.
Wenig Text- lassen Sie die Bilder sprechen!!
Der Flyer soll lust auf eine Tour bei uns machen!
Der Flyer soll natürlich wirken.
Unsere CI wird schon durch unser Logo mitgegeben- es müssen nicht unbeding gr. Flächen mit unseren Farben gefüllt werden!!
Uns sprechen filigrane, künstlerische Designs an. Aber bitte die natürlichkeit nicht aus den Augen verlieren. Wir sind OUTDOORveranstalter- unsere Aktionen finden in der Natur statt!
Eine Variante, die ich aus zahlreichen Designs erarbeitet habe:
Nutzen Sie ein grosses Bild als Header (Kopfzeile) das auch z.B. im Orangeton (Logofarbe) überzeichnet - oder auch nur weiss (milchig) verändert sein darf.
Hierauf einen geeigneten Sinnspruch (Überschrift) z.B. "..mehr als nur ein Abenteuer"
der passend sein muss.
Etwas Poetisches vielleicht.... kurz und prägnant. (Natur, ökologie, Wasser, reisen...).
Bilder groß und darauf überlagert kleinere eingefasst in Rahmen.
Zum Textinhalt
Titelseite:
was machen wir?
Paddel- & Radtouren im Weser-Leinebergland, tolles Bild und unser Logo
evtl. noch für wen geeignet?
Schulklassen, Betriebe, Vereine, Familien, Junggesellenabschiede etc.
Innenseite(n):
Bilder, Bilder, Bilder (vielleicht gr. Hintergrundbild, dann kleine Bilder drauf mit passender Überschrift: z.B. Abenteuer im Tivorunde, Stand up paddling, Teambuilding Flossbau, Radverleih, Strudel & Speiche, usw.
Rückseite:
Unsere Kontaktdaten
Firmenname
Webseite
Mailadresse
Hausanschrift
plaudernetz
QR Code
LOGO
Toll wäre ein..

```html
<!DOCTYPE html>
<html lang="de">
<head>
<meta charset="utf-8">
<title>Flussfreude Faltflyer</title>
<link rel="stylesheet" href="https://fonts.googleapis.com/css2?family=Titillium+Web:wght@400;600&family=Open+Sans:wght@400;600&display=swap">
<style>
:root{
  --bg:#5b7383;
  --orange:#e48d1b;
  --orange-deep:#d9780f;
  --red:#8b1f12;
  --blue:#1f5b78;
  --blue-light:#d3e3ee;
  --ink:#2b2b2b;
  --line:#c9c9c9;
  --white:#ffffff;
}
*{margin:0;padding:0;box-sizing:border-box}
html,body{width:870px;height:1200px;overflow:hidden;background:var(--bg)}
.canvas{position:relative;width:870px;height:1200px}
.sheet{position:absolute;left:15px;width:840px;height:560px;overflow:hidden;background:var(--white);box-shadow:0 6px 18px rgba(0,0,0,.3)}
.sheet--outside{top:20px}
.sheet--inside{top:620px}
.panel{position:absolute;top:0;height:560px;width:280px;overflow:hidden}
.photo{position:absolute}
h2,h3,.brand{font-family:"Titillium Web",sans-serif;font-weight:400}
p,li,.contact{font-family:"Open Sans",sans-serif}
.body-text{font-size:8.4px;line-height:14px}

/* outside: intro panel */
.intro{left:0;background:linear-gradient(180deg,var(--orange) 0%,var(--orange-deep) 100%)}
.intro .photo{left:0;top:0;width:280px;height:215px;background:linear-gradient(160deg,#5f8a3a 0%,#3d5f2a 45%,#b4352b 75%,#d9d9d9 100%)}
.intro h2{position:absolute;left:40px;top:228px;font-size:26px;font-weight:600;color:var(--red)}
.intro .kicker{position:absolute;left:88px;top:260px;font-family:"Titillium Web",sans-serif;font-size:13px;color:var(--white);letter-spacing:.3px}
.intro .body-text{position:absolute;left:44px;top:290px;width:210px;color:var(--white)}
.intro .body-text + .body-text{top:405px}

/* outside: service panel */
.services{left:280px;background:var(--white);border-left:1px solid #e6e6e6}
.services h3{position:absolute;left:20px;font-size:15px;color:var(--red)}
.services ul{position:absolute;left:20px;width:200px;list-style:none}
.services li{position:relative;padding-left:22px;height:18px;font-size:8px;line-height:18px;color:var(--ink);border-bottom:1px solid var(--line)}
.services li svg{position:absolute;left:0;top:3px}
.services .brand{position:absolute;left:115px;top:418px;font-size:15px;font-weight:600;color:var(--orange-deep)}
.contact{position:absolute;left:103px;top:443px;font-size:7px;line-height:10px;color:#555}
.contact dl{margin-top:8px;display:grid;grid-template-columns:26px 1fr}
.contact dt{color:var(--red);font-size:5.5px}

/* outside: cover */
.cover{left:560px;background:linear-gradient(180deg,#f4f4f4 0%,#fff 22%,#c4dcea 27%,#7fb1d0 40%)}
.cover .brand{position:absolute;left:0;right:0;top:50px;text-align:center;font-size:24px;font-weight:600;color:var(--orange-deep)}
.cover h2{position:absolute;left:20px;top:148px;font-size:19px;font-weight:600;color:var(--red)}
.cover .kicker{position:absolute;left:20px;top:176px;font-family:"Titillium Web",sans-serif;font-size:10px;color:var(--orange-deep)}
.cover .photo{left:0;top:205px;width:280px;height:235px;background:linear-gradient(180deg,#8fbcd8 0%,#5f8f5a 35%,#6aa7c0 60%,#2f6f8c 100%)}
.cover .footer{position:absolute;left:0;top:430px;width:280px;height:130px;background:linear-gradient(180deg,rgba(31,91,120,0) 0%,var(--blue) 25%,#194b64 100%)}
.cover .footer h3{position:absolute;left:50px;top:42px;font-size:14px;color:var(--orange)}
.cover .footer p{position:absolute;left:50px;top:66px;font-family:"Titillium Web",sans-serif;font-size:10px;line-height:13px;color:var(--white)}

/* inside: adventure spread */
.spread{left:0;width:560px;background:linear-gradient(180deg,#e9f1f6 0%,var(--blue-light) 30%,#a9c8dc 55%)}
.spread h2{position:absolute;left:30px;top:26px;font-size:26px;font-weight:600;color:var(--orange-deep)}
.spread .kicker{position:absolute;left:30px;top:66px;font-family:"Titillium Web",sans-serif;font-weight:600;font-size:11px;color:var(--red)}
.spread .body-text{position:absolute;left:30px;top:120px;width:240px;color:var(--ink)}
.spread .hero{left:0;top:240px;width:560px;height:200px;background:linear-gradient(180deg,#9cbfd3 0%,#5d7f4a 40%,#48708a 70%,#2f5566 100%)}
.spread .band{position:absolute;left:0;top:420px}
.spread .strip-a{left:0;top:455px;width:280px;height:105px;background:linear-gradient(180deg,#bcd7e8 0%,#7c9a5c 60%,#5b8a3c 100%)}
.spread .strip-b{left:282px;top:455px;width:278px;height:105px;background:linear-gradient(180deg,#9fbfa0 0%,#6d9850 50%,#a83a30 100%)}
.frame{position:absolute;background:var(--white);padding:5px;box-shadow:0 2px 6px rgba(0,0,0,.35)}
.frame .photo{position:static;width:100%;height:100%}
.frame-1{left:335px;top:90px;width:160px;height:120px;transform:rotate(3deg)}
.frame-1 .photo{background:linear-gradient(160deg,#8fb4c9,#4f7a45 55%,#3d6780)}
.frame-2{left:425px;top:190px;width:105px;height:75px;transform:rotate(-4deg)}
.frame-2 .photo{background:linear-gradient(160deg,#a7c6d9,#5e8b4a 60%,#b23a2e)}
.frame-3{left:330px;top:250px;width:130px;height:95px;transform:rotate(-6deg)}
.frame-3 .photo{background:linear-gradient(160deg,#6f8e4c,#8ba1a9 60%,#b13a2f)}
.frame-4{left:428px;top:298px;width:105px;height:75px;transform:rotate(3deg)}
.frame-4 .photo{background:linear-gradient(160deg,#89b4cc,#4c7f9a 60%,#b73b30)}

/* inside: more offers */
.offers{left:560px;background:var(--white)}
.offers .photo-top{left:0;top:0;width:280px;height:245px;background:linear-gradient(180deg,#88a96c 0%,#6f9450 50%,#d7dcd3 85%,#fff 100%)}
.offers .dot{position:absolute;left:228px;top:226px;width:26px;height:26px;border-radius:50%;background:var(--orange)}
.offers h3{position:absolute;left:30px;top:252px;font-size:16px;color:var(--red)}
.offers .body-text{position:absolute;left:30px;top:288px;width:222px;color:var(--ink)}
.offers .photo-bottom{left:0;top:455px;width:280px;height:105px;background:linear-gradient(180deg,#fff 0%,#c9c9c9 30%,#b9302a 65%,#c8d3da 100%)}
</style>
</head>
<body>
<main class="canvas">

  <section class="sheet sheet--outside">
    <article class="panel intro">
      <div class="photo" role="img" aria-label="Foto: Jugendliche mit Paddeln im roten Kanu auf einem grünen Flussufer"></div>
      <h2>Der Natur</h2>
      <div class="kicker">EIN STÜCK NÄHER</div>
      <p class="body-text">Wir sind Ihr individueller Anbieter für Kanu-, Rad- und Erlebnistouren im Weser- und Leine­bergland. Wir bieten Touren ab Hann.-Münden, Bad Karlshafen, Beverungen, Höxter, Holzminden, Polle, Bodenwerder, Hameln, Rinteln, Vlotho, Bad Oeynhausen, Porta Westfalica und Minden an.</p>
      <p class="body-text">Mitten im Herzen Deutschlands organisieren wir Ihre Betriebs-, Gruppen-, und Schulklassen­ausfahrt zu fairen Preisen auf der Weser, Leine, Emmer, Diemel, Nethe, und Innerste. Auch Einzelreisende und Familien sind bei uns richtig, wenn es darum geht eine schöne Zeit draußen zu verbringen.</p>
    </article>

    <article class="panel services">
      <h3 style="top:76px">Wir vermieten:</h3>
      <ul style="top:104px">
        <li><svg width="13" height="12" viewBox="0 0 13 12"><polyline points="1,6 5,10 12,1" fill="none" stroke="#e48d1b" stroke-width="2.6"/></svg>Kanus</li>
        <li><svg width="13" height="12" viewBox="0 0 13 12"><polyline points="1,6 5,10 12,1" fill="none" stroke="#e48d1b" stroke-width="2.6"/></svg>Schlauchboote (Rafts)</li>
        <li><svg width="13" height="12" viewBox="0 0 13 12"><polyline points="1,6 5,10 12,1" fill="none" stroke="#e48d1b" stroke-width="2.6"/></svg>SUP (Stand up Paddling)</li>
        <li style="border-bottom:0"><svg width="13" height="12" viewBox="0 0 13 12"><polyline points="1,6 5,10 12,1" fill="none" stroke="#e48d1b" stroke-width="2.6"/></svg>Fahrräder</li>
      </ul>
      <h3 style="top:204px">Wir oragnisieren:</h3>
      <ul style="top:232px">
        <li><svg width="13" height="12" viewBox="0 0 13 12"><polyline points="1,6 5,10 12,1" fill="none" stroke="#e48d1b" stroke-width="2.6"/></svg>Bogenschießen</li>
        <li><svg width="13" height="12" viewBox="0 0 13 12"><polyline points="1,6 5,10 12,1" fill="none" stroke="#e48d1b" stroke-width="2.6"/></svg>Floßtouren</li>
        <li><svg width="13" height="12" viewBox="0 0 13 12"><polyline points="1,6 5,10 12,1" fill="none" stroke="#e48d1b" stroke-width="2.6"/></svg>Nordic Walking</li>
        <li><svg width="13" height="12" viewBox="0 0 13 12"><polyline points="1,6 5,10 12,1" fill="none" stroke="#e48d1b" stroke-width="2.6"/></svg>Abenteuer Großkanu</li>
        <li><svg width="13" height="12" viewBox="0 0 13 12"><polyline points="1,6 5,10 12,1" fill="none" stroke="#e48d1b" stroke-width="2.6"/></svg>Tages- und Mehrtagestouren</li>
        <li style="border-bottom:0"><svg width="13" height="12" viewBox="0 0 13 12"><polyline points="1,6 5,10 12,1" fill="none" stroke="#e48d1b" stroke-width="2.6"/></svg>Schulklassenausflüge</li>
      </ul>
      <div class="brand">flussfreude.de</div>
      <div class="contact">
        Flussfreude<br>Kanutouristik<br>Helga Sandmann<br>Uferweg 4<br>37999 Beispielheim
        <dl>
          <dt>TEL.</dt><dd>(0 12 34) 56 78 90</dd>
          <dt>MOBIL</dt><dd>(0 15 00) 12 34 567</dd>
          <dt style="margin-top:8px">WEB</dt><dd style="margin-top:8px">www.flussfreude-beispiel.de</dd>
        </dl>
      </div>
    </article>

    <article class="panel cover">
      <div class="brand">flussfreude.de</div>
      <h2>Paddeltouren</h2>
      <div class="kicker">AUF DER WESER UND IM UMLAND</div>
      <div class="photo" role="img" aria-label="Foto: Gruppe im Schlauchboot hebt jubelnd die Paddel, Burg am Ufer"></div>
      <div class="footer">
        <h3>Paddeltouren auf der Weser</h3>
        <p>FÜR GRUPPEN WIE VEREINE,<br>SCHULKLASSEN UND FAMILIEN</p>
      </div>
    </article>
  </section>

  <section class="sheet sheet--inside">
    <article class="panel spread">
      <h2>... mehr als nur ein Abenteuer!</h2>
      <div class="kicker">NATURERLEBNISSE FÜR GROSS &amp; KLEIN</div>
      <p class="body-text">Die Gewässer Weser und Leine spielen eine große Rolle. Auf der Weser bieten sich optimale Mehrtagestouren mit Übernachtungen in den verschiedensten Kategorien an. Aber auch die Leine birgt Ihre ganz speziellen Reize. Mit unseren Hannovertouren z.B. bieten wir seit Jahren Touren für kleinere sowie größere Gruppen an, um unsere schöne Landeshauptstadt einmal aus einer ganz anderen Perspektive kennenzulernen.</p>
      <div class="photo hero" role="img" aria-label="Foto: rotes Kanu auf dem Fluss vor einer steinernen Bogenbrücke"></div>
      <div class="frame frame-1"><div class="photo" role="img" aria-label="Foto: Kinder mit Schwimmwesten im Kanu"></div></div>
      <div class="frame frame-2"><div class="photo" role="img" aria-label="Foto: Kanus am Flussufer"></div></div>
      <div class="frame frame-3"><div class="photo" role="img" aria-label="Foto: Gruppe paddelt im Kanu"></div></div>
      <div class="frame frame-4"><div class="photo" role="img" aria-label="Foto: Schlauchboot auf dem Wasser"></div></div>
      <svg class="band" width="560" height="40" viewBox="0 0 560 40"><path d="M0 8 Q280 40 560 4 L560 36 L0 36 Z" fill="#ffffff"/><path d="M0 8 Q280 40 560 4 L560 12 Q280 46 0 16 Z" fill="#e48d1b"/></svg>
      <div class="photo strip-a" role="img" aria-label="Foto: Tipizelte auf einer Wiese am Fluss"></div>
      <div class="photo strip-b" role="img" aria-label="Foto: Gruppe mit roten Kanus auf einer Wiese"></div>
    </article>

    <article class="panel offers">
      <div class="photo photo-top" role="img" aria-label="Foto: junge Frau beim Bogenschießen auf eine Zielscheibe"></div>
      <span class="dot"></span>
      <h3>Weitere Angebote</h3>
      <p class="body-text">Wir bieten Ihnen das instinktive Bogenschießen als Baustein für Ihre Kanu-Tour, oder als Schnupperkurs an. Wann haben Sie sich in dieser hektischen Zeit zuletzt einmal nur auf Ihren Instikt verlassen? In einer Welt, die voll ist mit technischen Finessen und immer bequemer werdenden Anwendungen ist uns der Bezug zum eigentlichen Leben fast gänzlich verloren gegangen. Wir wollen Ihnen zeigen, wie Sie sich wieder auf Ihren natürlichen Instinkt verlassen können. Weitere Informationen finden Sie auf unserer Website!</p>
      <div class="photo photo-bottom" role="img" aria-label="Foto: drei Mädchen paddeln im roten Kanu"></div>
    </article>
  </section>

</main>
</body>
</html>
```